VANDIR/ VANDIR GREY Business Card

We have two brands that we would like to show one 1 business card (front and back). We would to incorporate two different logos on one card (VANDIR and VANDIR GREY). Card can be two sided. Simple, sleek and professional.

We are a senior living provider.

www.vandir-example.com
www.vandirgrey-example.com

Target Market(s)

Professionals

Industry/Entity Type

Business

Font styles to use
Serif

Colors

Designer to choose colors to be used in the design.

Requirements
Must have
• Space for EMAIL, PHONE, WEBSITE
Nice to have
• Raised lettering or gloss lettering

```html
<!DOCTYPE html>
<html lang="en">
<head>
<meta charset="utf-8">
<title>Vandir / Vandir Grey Business Card</title>
<link href="https://fonts.googleapis.com/css2?family=Cinzel:wght@500&family=Open+Sans:wght@400;600;700&display=swap" rel="stylesheet">
<style>
  :root {
    --backdrop: #8a8b8b;
    --card: #1d1d1d;
    --gold: #d4ab3c;
    --gold-soft: #c9a237;
  }
  html, body {
    margin: 0;
    padding: 0;
    width: 1200px;
    height: 781px;
    overflow: hidden;
    background: var(--backdrop);
  }
  .canvas {
    position: relative;
    width: 1200px;
    height: 781px;
  }
  .card {
    position: absolute;
    left: 357px;
    width: 454px;
    height: 252px;
    background: var(--card);
    color: var(--gold);
  }
  .card--front { top: 102px; }
  .card--back { top: 409px; }

  .brand-name {
    font-family: "Cinzel", serif;
    font-weight: 500;
    color: var(--gold);
    white-space: nowrap;
    line-height: 1;
  }
  .brand-name--front {
    position: absolute;
    left: 0;
    right: 0;
    top: 44px;
    text-align: center;
    font-size: 36px;
    letter-spacing: 1px;
  }

  .lockup {
    position: absolute;
    left: 0;
    right: 0;
    top: 106px;
    display: flex;
    flex-direction: column;
    align-items: center;
  }
  .brand-name--back {
    font-size: 27px;
    letter-spacing: 0.5px;
  }
  .tagline {
    margin-top: 5px;
    font-family: "Open Sans", sans-serif;
    font-size: 11.5px;
    line-height: 14px;
    color: var(--gold-soft);
    white-space: nowrap;
  }

  .holder {
    position: absolute;
    right: calc(454px - 218px);
    top: 160px;
    text-align: right;
    font-family: "Open Sans", sans-serif;
    font-size: 11px;
    line-height: 15px;
    color: var(--gold-soft);
    white-space: nowrap;
  }
  .holder__name {
    font-size: 15px;
    font-weight: 700;
    line-height: 19px;
    color: var(--gold);
  }
  .divider {
    position: absolute;
    left: 234px;
    top: 156px;
    width: 1px;
    height: 61px;
    background: var(--gold-soft);
  }
  .contacts {
    position: absolute;
    left: 249px;
    top: 164px;
    margin: 0;
    padding: 0;
    list-style: none;
    font-family: "Open Sans", sans-serif;
    font-size: 11px;
    line-height: 15px;
    color: var(--gold-soft);
  }
  .contacts li {
    display: flex;
    align-items: center;
    gap: 7px;
    white-space: nowrap;
  }
  .contacts svg {
    width: 9px;
    height: 9px;
    flex: none;
  }
</style>
</head>
<body>
<div class="canvas">

  <section class="card card--front" aria-label="Business card front">
    <div class="brand-name brand-name--front">VANDIR</div>

    <div class="holder">
      <div class="holder__name">Elena Marsh</div>
      <div class="holder__role">Manager</div>
      <div class="holder__address">12 Harbor Lane, Suite 4</div>
      <div class="holder__address">Fairview Park, CA 00000</div>
    </div>

    <div class="divider" aria-hidden="true"></div>

    <ul class="contacts">
      <li>
        <svg viewBox="0 0 10 10" aria-hidden="true"><path d="M2 1 L3.6 1 L4.2 3 L3.2 3.8 Q4 5.8 6.2 6.8 L7 5.8 L9 6.4 L9 8 Q8.5 9 7.5 9 Q1 8 1 2.5 Q1 1 2 1 Z" fill="var(--gold-soft)"/></svg>
        <span>+000 1234 5678</span>
      </li>
      <li>
        <svg viewBox="0 0 10 10" aria-hidden="true"><rect x="0.5" y="2" width="9" height="6.5" rx="0.8" fill="var(--gold-soft)"/><path d="M0.8 2.5 L5 5.6 L9.2 2.5" stroke="var(--card)" stroke-width="0.9" fill="none"/></svg>
        <span>info@vandir-example.com</span>
      </li>
      <li>
        <svg viewBox="0 0 10 10" aria-hidden="true"><circle cx="5" cy="5" r="4.5" fill="var(--gold-soft)"/><path d="M0.8 5 H9.2 M5 0.6 Q2.6 5 5 9.4 M5 0.6 Q7.4 5 5 9.4" stroke="var(--card)" stroke-width="0.8" fill="none"/></svg>
        <span>www.vandir-example.com</span>
      </li>
      <li>
        <svg viewBox="0 0 10 10" aria-hidden="true"><circle cx="5" cy="5" r="4.5" fill="var(--gold-soft)"/><path d="M0.8 5 H9.2 M5 0.6 Q2.6 5 5 9.4 M5 0.6 Q7.4 5 5 9.4" stroke="var(--card)" stroke-width="0.8" fill="none"/></svg>
        <span>www.vandirgrey-example.com</span>
      </li>
    </ul>
  </section>

  <section class="card card--back" aria-label="Business card back">
    <div class="lockup">
      <div class="brand-name brand-name--back">VANDIR GREY</div>
      <div class="tagline">Refined Senior Living Residences</div>
    </div>
  </section>

</div>
</body>
</html>
```